DWR Logistics Marketing flyer

Good morning, I run a trucking company and I will be needing help setting up a website logo and a marketing flyer or something like that talking about our services and what we can offer to potential new customers who need to ship their product. I need help getting this all together.

Target Market(s)

Transportation customers

Requirements
Must have
• should list our services and contact info
Nice to have
• the Logo on the top

```html
<!DOCTYPE html>
<html lang="en">
<head>
<meta charset="utf-8">
<title>DWR Logistics – Services Flyer</title>
<link rel="stylesheet" href="https://fonts.googleapis.com/css2?family=Figtree:wght@400;700;800&family=Lato:wght@400;700&display=swap">
<style>
  :root {
    --backdrop: #2b2b2b;
    --paper: #ffffff;
    --charcoal: #45403d;
    --ink: #1c1c1c;
    --text-dark: #2a2a2a;
    --brand-blue: #1f7fdb;
    --brand-blue-deep: #1668c2;
    --cyan: #14c8f2;
    --icon-cyan: #12d0f7;
    --navy: #1b3f8f;
  }
  * { box-sizing: border-box; margin: 0; padding: 0; }
  html, body { width: 950px; height: 1200px; overflow: hidden; background: var(--backdrop); }
  body { font-family: "Lato", sans-serif; color: var(--text-dark); }

  .flyer {
    position: absolute; left: 50px; top: 50px;
    width: 850px; height: 1100px;
    background: var(--paper); overflow: hidden;
  }
  .backdrop-shapes { position: absolute; inset: 0; }

  .hero-title {
    position: absolute; left: 47px; top: 372px;
    font-family: "Figtree", sans-serif; font-weight: 400; font-size: 33px; line-height: 38px;
    color: #fff; letter-spacing: -0.3px;
  }
  .hero-title .light { font-weight: 400; }
  .hero-title .bold { font-weight: 800; }
  .hero-title .accent { font-weight: 800; color: var(--cyan); }

  .tagline {
    position: absolute; left: 49px; top: 493px; white-space: nowrap;
    font-family: "Figtree", sans-serif; font-weight: 700; font-size: 18.5px; color: #fff;
  }
  .intro {
    position: absolute; left: 49px; top: 524px; width: 356px;
    font-size: 16px; line-height: 20px; color: #fff;
  }

  .services {
    position: absolute; left: 449px; top: 292px; width: 344px; height: 435px;
    background: linear-gradient(160deg, var(--brand-blue) 0%, var(--brand-blue-deep) 100%);
    color: #fff;
  }
  .services-title {
    position: absolute; left: 0; right: 0; top: 20px; text-align: center;
    font-family: "Figtree", sans-serif; font-weight: 400; font-size: 21px; letter-spacing: 0.2px;
  }
  .services-title b { font-weight: 800; }
  .service {
    position: absolute; left: 37px; right: 24px; height: 60px;
    display: flex; align-items: center; justify-content: space-between;
    font-family: "Figtree", sans-serif; font-weight: 800; font-size: 19.5px; line-height: 25px;
  }
  .service svg { fill: var(--icon-cyan); display: block; }

  .section-title {
    position: absolute; font-weight: 400;
    font-family: "Figtree", sans-serif; font-size: 21px; line-height: 26px; color: var(--ink);
  }
  .section-title b { font-weight: 800; display: block; }

  .bullet-list { position: absolute; list-style: none; font-size: 15.3px; line-height: 18.5px; color: var(--text-dark); }
  .bullet-list li { position: relative; padding-left: 25px; margin-bottom: 5px; }
  .bullet-list svg { position: absolute; left: 0; top: 2px; }
  .highlights { left: 64px; top: 769px; width: 372px; }
  .advantages { left: 480px; top: 816px; width: 314px; }
  .advantages li { padding-left: 27px; margin-bottom: 4px; }

  .award-bar {
    position: absolute; left: 0; top: 969px; width: 650px; height: 55px;
    background: var(--brand-blue); color: #fff;
    padding: 8px 0 0 64px; font-size: 16px; line-height: 20px;
  }

  .clients-title {
    position: absolute; left: 634px; top: 955px; font-weight: 400;
    font-family: "Figtree", sans-serif; font-size: 21px; color: var(--brand-blue-deep); white-space: nowrap;
  }
  .clients-title b { font-weight: 800; }
  .client {
    position: absolute; display: flex; align-items: center; gap: 4px; transform: translateX(-50%);
    font-family: "Figtree", sans-serif; font-weight: 800; font-size: 13px; color: var(--navy); white-space: nowrap;
  }
  .client i { width: 9px; height: 9px; border-radius: 50%; background: var(--navy); display: block; }

  .contact {
    position: absolute; top: 1044px; font-size: 16px; line-height: 20px; color: var(--ink);
  }
  .contact b { font-weight: 700; }
  .address { left: 63px; font-size: 17px; }
  .officers { left: 334px; }
  .divider { position: absolute; left: 317px; top: 1051px; width: 2px; height: 32px; background: var(--navy); }
</style>
</head>
<body>
<main class="flyer">
  <svg class="backdrop-shapes" width="850" height="1100" viewBox="0 0 850 1100">
    <defs>
      <linearGradient id="skyRoad" x1="0" y1="0" x2="0" y2="1">
        <stop offset="0" stop-color="#a9c7e8"/>
        <stop offset="0.55" stop-color="#d9e6f2"/>
        <stop offset="0.62" stop-color="#7f9a5a"/>
        <stop offset="0.7" stop-color="#c9cdd1"/>
        <stop offset="1" stop-color="#b7bbbf"/>
      </linearGradient>
    </defs>
    <rect x="0" y="0" width="850" height="380" fill="url(#skyRoad)" role="img" aria-label="Photo of a white semi truck with a blue curtain-side trailer on a highway"/>
    <polygon points="0,367 850,307 850,633 0,693" fill="var(--charcoal)"/>
    <polygon points="0,693 850,633 850,636 0,697" fill="#ffffff"/>
    <polygon points="610,948 850,948 850,1100 667,1100" fill="var(--cyan)"/>
  </svg>

  <h1 class="hero-title">
    <span class="light">DELIVERING</span><br>
    <span class="bold">EXCELLENCE IN</span><br>
    <span class="accent">LOGISTICS SINCE 2010</span>
  </h1>
  <p class="tagline">Efficient, Reliable, Nationwide Logistics</p>
  <p class="intro">We are a transportation company that specializes in logistics to maximize efficiency in getting the product from shipper to customer in the shortest, safest time possible. With our current 30 truck fleet, we can service customers locally and across the country with solo and team drivers to ensure timely delivery.</p>

  <section class="services">
    <h2 class="services-title">SERVICES <b>OFFERED</b></h2>
    <div class="service" style="top:70px;">
      <span>DRY VAN</span>
      <svg width="164" height="46" viewBox="0 0 164 46"><rect x="0" y="0" width="116" height="32" rx="3"/><path d="M119 2h16l10 16 16 6v14h-42z"/><circle cx="8" cy="39" r="6"/><circle cx="23" cy="39" r="6"/><circle cx="97" cy="39" r="6"/><circle cx="112" cy="39" r="6"/><circle cx="150" cy="40" r="6"/></svg>
    </div>
    <div class="service" style="top:141px;">
      <span>FLATBED</span>
      <svg width="134" height="54" viewBox="0 0 134 54"><rect x="0" y="26" width="96" height="12" rx="3"/><path d="M96 2h14l10 22 14 8v10h-38z"/><circle cx="24" cy="42" r="10"/><circle cx="66" cy="42" r="10"/><circle cx="112" cy="42" r="10"/></svg>
    </div>
    <div class="service" style="top:213px;">
      <span>TANKER LOAD</span>
      <svg width="108" height="54" viewBox="0 0 108 54"><rect x="0" y="6" width="82" height="30" rx="15"/><rect x="26" y="0" width="14" height="8" rx="2"/><path d="M86 12h10l12 12v14h-22z"/><rect x="0" y="36" width="108" height="5"/><circle cx="22" cy="44" r="8"/><circle cx="38" cy="44" r="8"/><circle cx="92" cy="44" r="8"/></svg>
    </div>
    <div class="service" style="top:283px;">
      <span>REEFER</span>
      <svg width="120" height="56" viewBox="0 0 120 56"><rect x="0" y="6" width="26" height="5"/><rect x="4" y="18" width="22" height="5"/><rect x="0" y="30" width="26" height="5"/><rect x="30" y="0" width="58" height="42" rx="3"/><path d="M92 14h14l14 14v14h-28z"/><circle cx="42" cy="46" r="8"/><circle cx="106" cy="46" r="8"/></svg>
    </div>
    <div class="service" style="top:340px; height:80px;">
      <span>SOLO AND<br>TEAM DRIVER</span>
      <svg width="48" height="56" viewBox="0 0 70 80"><path d="M14 12c10-10 32-10 42 0v8H14z"/><circle cx="35" cy="32" r="15"/><path d="M4 80v-14c0-10 12-16 20-17l11 12 11-12c8 1 20 7 20 17v14z"/></svg>
    </div>
  </section>

  <h2 class="section-title" style="left:64px; top:698px;">OPERATIONAL<b>HIGHLIGHTS</b></h2>
  <ul class="bullet-list highlights">
    <li><svg width="16" height="14" viewBox="0 0 16 14"><rect x="1" y="3" width="10" height="10" fill="none" stroke="var(--brand-blue)" stroke-width="1.6"/><path d="M3 7l4 4 8-10" fill="none" stroke="var(--brand-blue)" stroke-width="2.2"/></svg>Handling more than half of the nation’s orange juice transport.</li>
    <li><svg width="16" height="14" viewBox="0 0 16 14"><rect x="1" y="3" width="10" height="10" fill="none" stroke="var(--brand-blue)" stroke-width="1.6"/><path d="M3 7l4 4 8-10" fill="none" stroke="var(--brand-blue)" stroke-width="2.2"/></svg>Hauling corn oil for one of the nation's largest potato chip suppliers.</li>
    <li><svg width="16" height="14" viewBox="0 0 16 14"><rect x="1" y="3" width="10" height="10" fill="none" stroke="var(--brand-blue)" stroke-width="1.6"/><path d="M3 7l4 4 8-10" fill="none" stroke="var(--brand-blue)" stroke-width="2.2"/></svg>Transporting wine and alcohol across the country.</li>
    <li><svg width="16" height="14" viewBox="0 0 16 14"><rect x="1" y="3" width="10" height="10" fill="none" stroke="var(--brand-blue)" stroke-width="1.6"/><path d="M3 7l4 4 8-10" fill="none" stroke="var(--brand-blue)" stroke-width="2.2"/></svg>Over 40 million gallons of orange juice hauled in the past year.</li>
    <li><svg width="16" height="14" viewBox="0 0 16 14"><rect x="1" y="3" width="10" height="10" fill="none" stroke="var(--brand-blue)" stroke-width="1.6"/><path d="M3 7l4 4 8-10" fill="none" stroke="var(--brand-blue)" stroke-width="2.2"/></svg>Millions of gallons of corn oil and wine transported annually.</li>
  </ul>

  <h2 class="section-title" style="left:473px; top:745px;">OUR<b>ADVANTAGES</b></h2>
  <ul class="bullet-list advantages">
    <li><svg width="18" height="18" viewBox="0 0 18 18"><circle cx="9" cy="9" r="8" fill="none" stroke="var(--brand-blue)" stroke-width="1.5"/><path d="M7 5l4 4-4 4" fill="none" stroke="var(--brand-blue)" stroke-width="2"/></svg>Personalized customer service from pick-up to delivery.</li>
    <li><svg width="18" height="18" viewBox="0 0 18 18"><circle cx="9" cy="9" r="8" fill="none" stroke="var(--brand-blue)" stroke-width="1.5"/><path d="M7 5l4 4-4 4" fill="none" stroke="var(--brand-blue)" stroke-width="2"/></svg>Direct contact with the owner or decision-makers for quick problem-solving and execution.</li>
    <li><svg width="18" height="18" viewBox="0 0 18 18"><circle cx="9" cy="9" r="8" fill="none" stroke="var(--brand-blue)" stroke-width="1.5"/><path d="M7 5l4 4-4 4" fill="none" stroke="var(--brand-blue)" stroke-width="2"/></svg>Adaptable fleet size to meet customer needs.</li>
  </ul>

  <div class="award-bar">
    Northline carrier excellence award two years in a row<br>
    Number one truck supplier for two major orange juice manufacturers in the US.
  </div>

  <h2 class="clients-title">CLINET <b>REFERENCE</b></h2>
  <div class="client" style="left:706px; top:1018px;"><i></i>SUNVALE</div>
  <div class="client" style="left:792px; top:1003px;"><i></i>Crispfield</div>
  <div class="client" style="left:712px; top:1066px;"><i></i>Unibev</div>
  <div class="client" style="left:792px; top:1071px;"><i></i>Citrana</div>

  <p class="contact address"><b>412 Oak Ct. Jasper, IN. 47546</b><br>dwrlogisticsllc@dwrmail.com</p>
  <span class="divider"></span>
  <p class="contact officers">CEO: <b>Mark Halloway - 812-555-0142</b><br>CFO: <b>Ryan Tessler - 812-555-0187</b></p>
</main>
</body>
</html>
```